Stewardship Tide - Descriptive Diagram/Graphic of Concepts

Stewardship Tide is a personal change philosophy that focuses on the individual making six commitments - Authenticity, Curiosity, Vision, Passion, Courage, and Humility - and living a cycle of Balance, Sustainability, and Renewal. In a typical business presentation, the Six Commitments would be displayed as a pyramid (Authenticity as the Foundation, Humility as the pinnacle) and the cycle likely a circle with each concept running into each other.

The challenge then is two fold. I need a graphical representation of those concepts, but I need it integrated, so that the cycle supports the commitments. I am open to ideas but it should be something that can be used for print or graphic materials, as well as presented on a website. Colors do not matter, but it sould be colorful.

Industry/Entity Type

Graphic Design

```html
<!DOCTYPE html>
<html lang="en">
<head>
<meta charset="utf-8">
<title>Stewardship Tide</title>
<link rel="stylesheet" href="https://fonts.googleapis.com/css2?family=Orbitron:wght@900&family=Anton&family=Advent+Pro:wght@400;500&display=swap">
<style>
  :root {
    --frame: #e2e6ea;
    --frame-edge: #b9c0c7;
    --field-light: #8e9aa6;
    --field-dark: #717e8b;
    --ink: #0c0c0c;
    --peak: #d6d21a;
    --humility: #e88a1e;
    --courage: #e2463c;
    --passion: #d0215c;
    --vision: #7b2489;
    --curiosity: #26388e;
    --authenticity: #6c4c5c;
    --base-top: #f47c20;
    --base-bottom: #ff5a10;
    --balance: #1c1cf2;
    --sustainability: #2af2f2;
    --renewal: #22f022;
  }
  html, body {
    margin: 0;
    width: 1200px;
    height: 900px;
    overflow: hidden;
    background: var(--frame);
  }
  .canvas { display: block; width: 1200px; height: 900px; }
  .title {
    font-family: "Orbitron", sans-serif;
    font-weight: 900;
    font-size: 66px;
    paint-order: stroke;
    stroke: var(--ink);
    stroke-width: 9px;
    stroke-linejoin: round;
  }
  .commitment {
    font-family: "Anton", sans-serif;
    text-anchor: start;
  }
  .humility { fill: var(--humility); }
  .courage { fill: var(--courage); }
  .passion { fill: var(--passion); }
  .vision { fill: url(#visionTone); }
  .curiosity { fill: var(--curiosity); }
  .authenticity { fill: url(#authenticityTone); }
  .cycle {
    font-family: "Advent Pro", sans-serif;
    font-weight: 500;
  }
  .balance { fill: var(--balance); }
  .sustainability { fill: var(--sustainability); }
  .renewal { fill: var(--renewal); }
  .arrow { fill: var(--ink); }
  .arrow-line { fill: none; stroke: var(--ink); stroke-width: 14; stroke-linejoin: miter; }
</style>
</head>
<body>
<svg class="canvas" viewBox="0 0 1200 900" xmlns="http://www.w3.org/2000/svg" role="img" aria-label="Stewardship Tide: six commitments in a pyramid supported by a cycle of balance, sustainability and renewal">
  <defs>
    <linearGradient id="fieldTone" x1="0" y1="0" x2="0" y2="1">
      <stop offset="0" stop-color="var(--field-light)"/>
      <stop offset="1" stop-color="var(--field-dark)"/>
    </linearGradient>
    <linearGradient id="chrome" x1="0" y1="0" x2="0" y2="1">
      <stop offset="0" stop-color="#ffffff"/>
      <stop offset="0.45" stop-color="#d8dde2"/>
      <stop offset="0.55" stop-color="#8c949c"/>
      <stop offset="1" stop-color="#eef1f4"/>
    </linearGradient>
    <linearGradient id="baseTone" x1="0" y1="0" x2="0" y2="1">
      <stop offset="0" stop-color="var(--base-top)"/>
      <stop offset="1" stop-color="var(--base-bottom)"/>
    </linearGradient>
    <linearGradient id="peakTone" x1="0" y1="0" x2="0" y2="1">
      <stop offset="0" stop-color="#c9d21a"/>
      <stop offset="1" stop-color="#e0cc1c"/>
    </linearGradient>
    <linearGradient id="visionTone" x1="0" y1="0" x2="1" y2="0">
      <stop offset="0" stop-color="#6a2a8e"/>
      <stop offset="1" stop-color="#9a1f7a"/>
    </linearGradient>
    <linearGradient id="authenticityTone" x1="0" y1="0" x2="1" y2="0">
      <stop offset="0" stop-color="#5a4a66"/>
      <stop offset="1" stop-color="#8a4a4a"/>
    </linearGradient>
  </defs>

  <rect class="frame" x="3" y="3" width="1194" height="894" rx="28" fill="var(--frame)" stroke="var(--frame-edge)" stroke-width="3"/>
  <rect class="field" x="16" y="16" width="1168" height="868" rx="20" fill="url(#fieldTone)" stroke="#f4f6f8" stroke-width="3"/>

  <text class="title" x="603" y="92" text-anchor="middle" textLength="740" lengthAdjust="spacingAndGlyphs" fill="url(#chrome)">STEWARDSHIP TIDE</text>

  <polygon class="peak" points="584,105 668,172 500,172" fill="url(#peakTone)"/>
  <text class="commitment humility" x="490" y="240" font-size="56" textLength="187" lengthAdjust="spacingAndGlyphs">HUMILITY</text>
  <text class="commitment courage" x="469" y="311" font-size="64" textLength="222" lengthAdjust="spacingAndGlyphs">COURAGE</text>
  <text class="commitment passion" x="439" y="387" font-size="74" textLength="274" lengthAdjust="spacingAndGlyphs">PASSION</text>
  <text class="commitment vision" x="416" y="481" font-size="88" textLength="328" lengthAdjust="spacingAndGlyphs">VISION</text>
  <text class="commitment curiosity" x="384" y="568" font-size="92" textLength="384" lengthAdjust="spacingAndGlyphs">CURIOSITY</text>
  <text class="commitment authenticity" x="340" y="662" font-size="98" textLength="469" lengthAdjust="spacingAndGlyphs">AUTHENTICITY</text>
  <path class="base" d="M296,677 H848 L860,692 V744 L848,759 H296 L285,744 V692 Z" fill="url(#baseTone)"/>

  <text class="cycle balance" x="41" y="469" font-size="96" textLength="281" lengthAdjust="spacingAndGlyphs">BALANCE</text>
  <text class="cycle sustainability" x="832" y="481" font-size="116" textLength="311" lengthAdjust="spacingAndGlyphs">SUSTAINABILITY</text>
  <text class="cycle renewal" x="413" y="862" font-size="110" textLength="288" lengthAdjust="spacingAndGlyphs">RENEWAL</text>

  <path class="arrow" d="M214,252 Q262,204 352,208 L338,192 L404,220 L340,246 L352,226 Q272,224 240,286 Q212,274 214,252 Z"/>
  <path class="arrow-line" d="M893,180 H960 V250"/>
  <polygon class="arrow" points="940,248 980,248 960,282"/>
  <path class="arrow" d="M998,760 Q952,808 866,808 L878,826 L814,798 L878,770 L868,790 Q942,790 978,730 Q1004,740 998,760 Z"/>
  <path class="arrow-line" d="M270,812 H196 V752"/>
  <polygon class="arrow" points="176,754 216,754 196,722"/>
</svg>
</body>
</html>
```